Join Our Real Estate Team

I would like to purchase a customized version of a design you have previously submitted - https://www.artpitchly.com/design/61937402

I want to create a recruitment AD. I have attached a AD I have created and would like as much of this information on an AD as possible. My main GOAL is to promote $350 Flat Fee (Includes E&O) per Transaction & No Monthly Fees.
I like to use a photo stock as I have in the attachment of various people.
I DON'T want to say "Wanted". Prefer to say something like "STOP Paying High Splits...Keep Most of YOUR hard earned Commissions"
Feel free to use other formats that might fit all the information that I have in my flyer I have uploaded.

Target Market(s)

Realtors

Industry/Entity Type

Real Estate

Font styles to use
Serif

Colors
0094D4
00A9DD
6FCCEA
C7EBF8
E9F6FB

Requirements
Must have
• See uploaded flyer to get must haves
Nice to have
• See uploaded flyer to get ideas
Should not have
• Do not want it to say "wanted"

```html
<!DOCTYPE html>
<html lang="en">
<head>
<meta charset="utf-8">
<title>Join Our Team – Coastal Keys Realty Group</title>
<link href="https://fonts.googleapis.com/css2?family=Open+Sans:wght@400;600;700&family=Lora:wght@700&display=swap" rel="stylesheet">
<style>
  :root{
    --backdrop:#c9cacc;
    --paper:#ffffff;
    --teal:#5bc4cb;
    --ink:#2a2a2a;
    --ink-soft:#555555;
    --grey-text:#6a6a6a;
    --dark-bar:#2b2b2b;
    --rule:#c8c8c8;
  }
  *{margin:0;padding:0;box-sizing:border-box}
  html,body{width:1200px;height:1137px;overflow:hidden;background:var(--backdrop)}
  body{font-family:"Open Sans",Arial,sans-serif;position:relative}
  .ad{position:absolute;left:152px;top:105px;width:913px;height:913px;background:var(--paper);overflow:hidden}
  .team-photo{position:absolute;left:0;top:0;width:913px;height:463px;
    background:linear-gradient(100deg,#6e5a4c 0%,#9a8777 25%,#c9c1b8 55%,#8d8c96 80%,#b6aea6 100%)}
  .brand{position:absolute;left:17px;top:0;width:203px;height:141px;background:var(--paper);
    display:flex;flex-direction:column;align-items:center;justify-content:center;gap:10px}
  .brand-mark{width:22px;height:22px;background:var(--teal);border-radius:50%}
  .brand-name{font-family:"Lora",Georgia,serif;font-weight:700;font-size:17px;line-height:1.2;color:var(--ink);text-align:center;letter-spacing:.5px}
  .brand-ribbon{position:absolute;left:17px;top:141px;width:203px;height:18px}
  .headline-band{position:absolute;left:0;top:406px;width:838px;height:124px;background:var(--teal);
    clip-path:polygon(0 0,806px 0,838px 124px,0 124px);
    color:#fff;font-weight:700;font-size:27px;line-height:1.5;padding:16px 0 0 29px;letter-spacing:.2px}
  .perk{position:absolute;display:flex;gap:14px}
  .perk svg{flex:none;margin-top:6px}
  .perk h3{font-size:25px;font-weight:700;color:var(--ink);line-height:1.15}
  .perk.small h3{font-size:20px}
  .perk p{font-size:18px;color:var(--ink-soft);line-height:1.3}
  .perk-fee{left:34px;top:560px}
  .perk-transaction{left:34px;top:645px}
  .perk-example{left:458px;top:560px}
  .perk-join{left:458px;top:645px}
  .call-label{position:absolute;left:41px;top:738px;width:372px;text-align:center;font-size:30px;font-weight:600;color:var(--grey-text)}
  .phone-pill{position:absolute;left:41px;top:782px;width:372px;height:59px;border-radius:30px;background:var(--teal);
    box-shadow:0 0 0 3px #e4f4f5,0 4px 8px rgba(0,0,0,.15);color:#fff;font-size:42px;font-weight:600;
    display:flex;align-items:center;justify-content:center;letter-spacing:1px}
  .contact-line{position:absolute;display:flex;align-items:center;gap:10px;font-size:19px;white-space:nowrap}
  .website{left:30px;top:852px;color:var(--teal);font-weight:700}
  .address{left:454px;top:852px;color:var(--ink-soft)}
  .divider{position:absolute;left:459px;top:758px;width:2px;height:80px;background:var(--rule)}
  .email-block{position:absolute;left:478px;top:762px;font-size:23px;color:var(--grey-text);line-height:1.5;white-space:nowrap}
  .email-block strong{color:var(--ink);font-weight:600}
  .base-bar{position:absolute;left:0;bottom:0;width:913px;height:14px;display:flex}
  .base-bar .dark{width:458px;background:var(--dark-bar)}
  .base-bar .accent{flex:1;background:var(--teal)}
</style>
</head>
<body>
<main class="ad">
  <div class="team-photo" role="img" aria-label="Stock photo of a smiling group of diverse real estate agents seated at a conference table"></div>

  <div class="brand">
    <span class="brand-mark"></span>
    <span class="brand-name">COASTAL KEYS<br>REALTY GROUP</span>
  </div>
  <svg class="brand-ribbon" viewBox="0 0 203 18" aria-hidden="true">
    <polygon points="0,0 203,0 203,6 101,18 0,6" fill="#5bc4cb"/>
  </svg>

  <div class="headline-band">STOP PAYING HIGH SPLITS...<br>KEEP MOST OF YOUR HARD EARNED COMMISSIONS</div>

  <div class="perk perk-fee">
    <svg width="20" height="20" viewBox="0 0 20 20"><circle cx="10" cy="10" r="10" fill="#5bc4cb"/><path d="M5.5 10.2l3 3 6-6.2" stroke="#fff" stroke-width="2.2" fill="none"/></svg>
    <div><h3>$350 FLAT FEE</h3><p>Includes E&amp;</p></div>
  </div>
  <div class="perk perk-transaction">
    <svg width="20" height="20" viewBox="0 0 20 20"><circle cx="10" cy="10" r="10" fill="#5bc4cb"/><path d="M5.5 10.2l3 3 6-6.2" stroke="#fff" stroke-width="2.2" fill="none"/></svg>
    <div><h3>PER TRANSACTION</h3><p>No Monthly Fees Timely Payouts</p></div>
  </div>
  <div class="perk small perk-example">
    <svg width="20" height="20" viewBox="0 0 20 20"><circle cx="10" cy="10" r="10" fill="#5bc4cb"/><path d="M5.5 10.2l3 3 6-6.2" stroke="#fff" stroke-width="2.2" fill="none"/></svg>
    <div><h3>ON A $250,000 SALE W/3% COMMISION</h3><p>$350 • Flat Fee = $ 7,150<br>Commision Earned w/CKRG</p></div>
  </div>
  <div class="perk perk-join">
    <svg width="20" height="20" viewBox="0 0 20 20"><circle cx="10" cy="10" r="10" fill="#5bc4cb"/><path d="M5.5 10.2l3 3 6-6.2" stroke="#fff" stroke-width="2.2" fill="none"/></svg>
    <div><h3>JOIN OUR TEAM</h3><p>Start Earning More Today</p></div>
  </div>

  <div class="call-label">CALL US TODAY AT</div>
  <div class="phone-pill">555 014 7391</div>

  <div class="contact-line website">
    <svg width="18" height="18" viewBox="0 0 20 20" aria-hidden="true"><circle cx="10" cy="10" r="10" fill="#5bc4cb"/><g stroke="#fff" stroke-width="1.3" fill="none"><circle cx="10" cy="10" r="6"/><ellipse cx="10" cy="10" rx="2.6" ry="6"/><path d="M4 10h12"/></g></svg>
    www.CoastalKeysRealtyGroup.com
  </div>

  <div class="divider"></div>
  <div class="email-block">or email us for more information at<br><strong>Dana@CKrealtyGroup.com</strong></div>

  <div class="contact-line address">
    <svg width="18" height="18" viewBox="0 0 20 20" aria-hidden="true"><circle cx="10" cy="10" r="10" fill="#5bc4cb"/><path d="M10 4.5a3.6 3.6 0 0 0-3.6 3.6c0 2.8 3.6 6.9 3.6 6.9s3.6-4.1 3.6-6.9A3.6 3.6 0 0 0 10 4.5z" fill="#fff"/><circle cx="10" cy="8.2" r="1.3" fill="#5bc4cb"/></svg>
    1287 Palmetto Ln, Harbor Springs, FL 34000
  </div>

  <div class="base-bar"><span class="dark"></span><span class="accent"></span></div>
</main>
</body>
</html>
```